custom window treatments and soft furnishings

letterhead design/logo
a simple design that can be used on my invoices as well as as a logo
could be needle and thread, fabric rolls, window with draperies or a abstract design

Reason: I have been traveling and unable to view the designs.

Target Market(s)

women 35 and up who purchase custom made products

```html
<!DOCTYPE html>
<html lang="en">
<head>
<meta charset="utf-8">
<title>Hemline Studio Letterhead</title>
<link rel="stylesheet" href="https://fonts.googleapis.com/css2?family=Merriweather:wght@900&family=PT+Sans+Narrow:wght@700&display=swap">
<style>
  :root {
    --paper: #ffffff;
    --ink: #111111;
    --accent: #2b78bd;
  }
  html, body {
    margin: 0;
    padding: 0;
    width: 900px;
    height: 1200px;
    overflow: hidden;
    background: var(--paper);
  }
  .letterhead {
    position: relative;
    width: 900px;
    height: 1200px;
    background: var(--paper);
    box-sizing: border-box;
    padding: 0 18px;
  }
  .brand {
    position: relative;
    height: 290px;
  }
  .brand-name {
    margin: 0;
    font-family: "Merriweather", Georgia, serif;
    font-weight: 900;
    color: var(--ink);
    line-height: 1;
  }
  .brand-name .line-main {
    position: absolute;
    left: 8px;
    top: 36px;
    font-size: 142px;
    letter-spacing: 2px;
  }
  .brand-name .line-sub {
    position: absolute;
    right: 96px;
    top: 190px;
    font-size: 84px;
  }
  .brand-dot {
    position: absolute;
    right: 6px;
    top: 200px;
    width: 72px;
    height: 72px;
    border-radius: 50%;
    background: var(--accent);
  }
  .rule {
    height: 22px;
    background: var(--accent);
    margin-top: 20px;
  }
  .contact {
    display: flex;
    justify-content: space-between;
    align-items: center;
    margin-top: 14px;
    font-family: "PT Sans Narrow", "Arial Narrow", sans-serif;
    font-weight: 700;
    font-size: 27px;
    color: var(--accent);
    white-space: nowrap;
  }
  .contact .address span + span {
    margin-left: 14px;
  }
  .separator {
    display: inline-block;
    width: 13px;
    height: 13px;
    background: var(--accent);
    transform: rotate(45deg);
  }
</style>
</head>
<body>
  <main class="letterhead">
    <header class="brand">
      <h1 class="brand-name">
        <span class="line-main">Hemline</span>
        <span class="line-sub">Studio</span>
      </h1>
      <div class="brand-dot" aria-hidden="true"></div>
    </header>
    <div class="rule" aria-hidden="true"></div>
    <p class="contact">
      <span class="address"><span>42 Linden Lane</span><span>Harborview RI 02811</span></span>
      <span class="separator" aria-hidden="true"></span>
      <span class="phone">401-555-0186</span>
      <span class="separator" aria-hidden="true"></span>
      <span class="email">hemlinestudio@mail.com</span>
    </p>
  </main>
</body>
</html>
```